Hollowbrook Renderworks Wordpress Design

I would like a design for my friends company. He has just had his logo designed and really likes the following website.

www.tbr-skimcoat.co.uk

Something similar to this design would be ideal but open to additional ideas. The website shown has all the relevant content.

We have 20 years of experience and can provide a number of photos for work we have done.

More photos will be provided upon request.

Target Market(s)

Homeowners

Industry/Entity Type

Trade

Font styles to use
Sans Serif

Colors
3176b5
85cae6
85abd2
eaf1f7

Requirements
Must have
• look at www.tbr-skimcoat.co.uk
Nice to have
Should not have
• N/A

```html
<!DOCTYPE html>
<html lang="en">
<head>
<meta charset="utf-8">
<title>Hollowbrook Renderworks</title>
<link href="https://fonts.googleapis.com/css2?family=Open+Sans:wght@400;600;700&family=Exo+2:wght@400;500&display=swap" rel="stylesheet">
<style>
:root{
  --blue:#3176b5;
  --sky:#85cae6;
  --steel:#85abd2;
  --mist:#eaf1f7;
  --cyan:#1fc3e8;
  --ink:#333;
  --text:#555;
  --muted:#666;
  --disc:#ececec;
  --band:#5b5b5b;
  --light:#f3f3f3;
}
*{margin:0;padding:0;box-sizing:border-box}
html,body{width:1200px;height:2790px;overflow:hidden}
body{font-family:"Open Sans",sans-serif;color:var(--text);background:#fff;position:relative}
.wrap{width:940px;margin:0 auto;position:relative}

.topbar{height:32px;background:var(--blue);color:#fff;font-size:12px}
.topbar .wrap{display:flex;justify-content:flex-end;align-items:center;height:32px;gap:20px}
.topbar span{display:flex;align-items:center;gap:6px}
.topbar .phone{font-size:13px}

.header{height:101px;border-bottom:1px solid #e3e3e3}
.header .wrap{display:flex;justify-content:space-between;align-items:center;height:100px}
.brand{display:flex;align-items:center;gap:10px}
.brand-mark{width:14px;height:14px;background:var(--blue)}
.brand-name{font-size:22px;font-weight:600;color:var(--blue);letter-spacing:.5px}
.nav{display:flex;gap:27px;font-size:13px;color:var(--muted);align-items:center}
.nav .active{color:var(--blue)}

.hero{height:376px;position:relative;background:linear-gradient(90deg,#e9e9e9 0%,#f7f7f7 45%,#ececec 70%,#d9c3b2 100%)}
.hero-form{position:absolute;left:665px;top:49px;width:360px}
.hero-form h1{font-size:29px;line-height:31px;color:var(--blue);font-weight:700}
.hero-form h2{font-size:19px;color:var(--ink);font-weight:700;margin:6px 0 12px}
.hero-form label{display:block;font-size:12px;color:var(--ink);margin:0 0 4px 4px}
.field{width:297px;height:32px;background:#fff;margin:0 0 20px 5px}
.btn-send{margin-left:5px;width:82px;height:32px;background:var(--blue);color:#fff;font-weight:700;font-size:13px;display:flex;align-items:center;justify-content:center;border-radius:2px}

.palette{position:absolute;left:1115px;top:480px;width:65px;height:206px;background:#fff;padding:10px 5px 0 16px;display:flex;flex-direction:column;gap:4px}
.palette i{display:block;width:46px;height:46px}

.intro-band{height:190px;background:var(--band);color:#fff;text-align:center;padding-top:44px}
.intro-band h2{font-size:28px;font-weight:700;margin-bottom:8px}
.intro-band p{font-size:14.5px;line-height:20px;width:940px;margin:0 auto}

.services{padding-top:50px;height:695px}
.section-title{font-size:29px;font-weight:700;color:var(--blue);text-align:center}
.service-grid{display:grid;grid-template-columns:repeat(3,1fr);column-gap:0;row-gap:16px;width:1000px;margin:36px auto 0}
.service{text-align:center;padding:0 30px}
.service .disc{width:96px;height:96px;border-radius:50%;background:var(--disc);margin:0 auto 12px;display:flex;align-items:center;justify-content:center}
.service h3{font-size:19px;color:var(--blue);font-weight:600;margin-bottom:12px}
.service p{font-size:11.5px;line-height:18.5px;color:var(--muted)}

.video-block{height:420px;background:var(--blue);color:#fff;padding-top:32px}
.video-block h2{font-family:"Exo 2",sans-serif;font-weight:400;font-size:31px;text-align:center}
.video-block h2 em{font-style:normal;color:var(--cyan);font-weight:500}
.video-row{display:flex;gap:29px;margin-top:25px}
.video{width:495px;height:277px;background:linear-gradient(135deg,#c98a5d,#e0a478 60%,#d39468);position:relative}
.play{position:absolute;left:215px;top:113px;width:52px;height:36px;background:#222;border-radius:7px;opacity:.85;display:flex;align-items:center;justify-content:center}
.video-copy h3{font-size:19px;font-weight:600;margin:13px 0 14px}
.video-copy p{font-size:13px;line-height:18.5px;width:400px}
.btn-free{margin-top:23px;width:145px;height:31px;background:var(--sky);color:#fff;font-weight:700;font-size:13px;display:flex;align-items:center;justify-content:center;border:1px solid #a9dcef}

.projects{height:368px;padding-top:44px;text-align:center}
.projects p{font-size:11.5px;color:var(--muted);margin:0 0 12px}
.project-strip{display:flex}
.project-strip div{width:235px;height:187px}
.p1{background:linear-gradient(180deg,#5a5552,#3c3631)}
.p2{background:linear-gradient(180deg,#9fb7d0,#6b5a4c)}
.p3{background:linear-gradient(180deg,#c8c0b5,#8c6e52)}
.p4{background:linear-gradient(180deg,#b49a74,#d8cc88)}

.testimonials{height:228px;background:var(--light);text-align:center;padding-top:32px}
.testimonials h4{font-size:16px;font-weight:600;color:#555;margin:18px 0 2px}
.testimonials p{font-size:11.5px;line-height:18.5px;color:var(--muted);width:800px;margin:0 auto}
.dots{display:flex;justify-content:center;gap:4px;margin-top:18px;padding-right:30px}
.dots i{width:12px;height:12px;border-radius:50%;background:#999}
.dots i:first-child{background:#444}

.footer{position:absolute;top:2461px;left:0;width:1200px;height:329px;background:var(--mist)}
.footer-cols{display:grid;grid-template-columns:315px 222px 227px 176px;padding-top:54px}
.footer h5{font-size:18px;font-weight:600;color:#444;margin-bottom:12px}
.footer p,.footer li{font-size:11.5px;line-height:17px;color:var(--muted);list-style:none}
.footer li{margin-bottom:6px}
.article{display:flex;gap:9px;padding-bottom:9px;margin-bottom:9px;border-bottom:1px solid #ccc;width:170px}
.article:last-child{border:0}
.thumb{width:41px;height:41px;background:linear-gradient(135deg,#6a3a3a,#c6b7a7)}
.article b{display:block;font-size:11.5px;color:#444;font-weight:600}
.article small{font-size:11.5px;color:var(--muted);display:flex;align-items:center;gap:5px}
.footer-bottom{position:absolute;top:258px;left:130px;width:940px;border-top:1px solid #c9c9c9;padding-top:21px;display:flex;justify-content:space-between;font-size:11.5px;color:#444}
.social{display:flex;gap:10px;margin-top:-3px}
.social i{width:22px;height:22px;border-radius:50%;background:var(--blue)}
</style>
</head>
<body>

<div class="topbar">
  <div class="wrap">
    <span><svg width="12" height="9" viewBox="0 0 12 9"><rect width="12" height="9" fill="#fff"/><path d="M0 0l6 5 6-5" stroke="#3176b5" fill="none"/></svg>hello@hollowbrookrenderworks.co.uk</span>
    <span class="phone"><svg width="8" height="12" viewBox="0 0 8 12"><rect x=".5" y=".5" width="7" height="11" rx="1" stroke="#fff" fill="none"/></svg>01632 960418</span>
  </div>
</div>

<header class="header">
  <div class="wrap">
    <div class="brand"><span class="brand-mark"></span><span class="brand-name">Hollowbrook Renderworks</span></div>
    <nav class="nav">
      <span class="active">Home</span><span>About</span><span>Our Projects</span><span>Services</span><span>Contact us</span>
      <svg width="11" height="11" viewBox="0 0 11 11"><circle cx="4.5" cy="4.5" r="3.5" stroke="#666" stroke-width="1.5" fill="none"/><path d="M7 7l3.5 3.5" stroke="#666" stroke-width="1.5"/></svg>
    </nav>
  </div>
</header>

<section class="hero" role="img" aria-label="Plasterer in white cap and gloves smoothing a wall with a trowel">
  <div class="hero-form">
    <h1>A Plasterer &nbsp;in Hollowbrook Renderworks</h1>
    <h2>-For homes and business</h2>
    <label>Your name:</label><div class="field"></div>
    <label>Your email:</label><div class="field"></div>
    <div class="btn-send">Send</div>
  </div>
</section>

<div class="palette">
  <i style="background:var(--blue)"></i><i style="background:var(--sky)"></i><i style="background:var(--steel)"></i><i style="background:var(--mist)"></i>
</div>

<section class="intro-band">
  <h2>We offer Plasterer Services in City?</h2>
  <p>Phasellus justo elit, vulputate interdum posuere eu, laoreet eget nibh. Aenean ut dapibus nisl. Vestibulum eu odio faucibus ligula vehicula iaculis. Maecenas augue sapien, posuere eu congue vitae, facilisis quis massa. Maecenas in risus lacus, quis feugiat enim. Maecenas ut orci libero. Phasellus iaculis eleifend dapibus.</p>
</section>

<section class="services">
  <h2 class="section-title">We offer Plasterer Services in City?</h2>
  <div class="service-grid">
    <div class="service">
      <div class="disc"><svg width="44" height="40" viewBox="0 0 44 40" fill="#3176b5"><path d="M2 40V16l10 6v-6l10 6v-6l10 6V6h8v34z"/><rect x="6" y="0" width="5" height="12"/></svg></div>
      <h3>Chimney Repairs</h3>
      <p>Lorem ipsum dolor sit amet, consectetur adipiscing elit. Etiam auctor tortor tellus, ut consectetur arcu. Nulla consequat egestas dapibus. Nullam eu quam sit amet justo imperdiet viverra. Vivamus leo lacus, interdum ac interdum</p>
    </div>
    <div class="service">
      <div class="disc"><svg width="42" height="42" viewBox="0 0 42 42" fill="none" stroke="#3176b5" stroke-width="3"><circle cx="21" cy="21" r="7"/><circle cx="21" cy="21" r="15" stroke-dasharray="6 3.4"/></svg></div>
      <h3>Rednering</h3>
      <p>Lorem ipsum dolor sit amet, consectetur adipiscing elit. Etiam auctor tortor tellus, ut consectetur arcu. Nulla consequat egestas dapibus. Nullam eu quam sit amet justo imperdiet viverra. Vivamus leo lacus, interdum ac interdum</p>
    </div>
    <div class="service">
      <div class="disc"><svg width="50" height="46" viewBox="0 0 50 46" fill="none" stroke="#3176b5" stroke-width="2"><path d="M4 40l24-24 14 8-24 20z"/><path d="M30 16l8-10 6 4-6 8"/></svg></div>
      <h3>Plastering</h3>
      <p>Lorem ipsum dolor sit amet, consectetur adipiscing elit. Etiam auctor tortor tellus, ut consectetur arcu. Nulla consequat egestas dapibus. Nullam eu quam sit amet justo imperdiet viverra. Vivamus leo lacus, interdum ac interdum</p>
    </div>
    <div class="service">
      <div class="disc"><svg width="50" height="44" viewBox="0 0 50 44" fill="#3176b5"><path d="M0 0h50v44H0z"/><path d="M8 6l17 12 17-12v32H8z" fill="#ececec"/><path d="M12 14l13 8 13-8v22H12z"/></svg></div>
      <h3>Ceilings</h3>
      <p>Lorem ipsum dolor sit amet, consectetur adipiscing elit. Etiam auctor tortor tellus, ut consectetur arcu. Nulla consequat egestas dapibus. Nullam eu quam sit amet justo imperdiet viverra. Vivamus leo lacus, interdum ac interdum</p>
    </div>
    <div class="service">
      <div class="disc"><svg width="48" height="46" viewBox="0 0 48 46" fill="none" stroke="#3176b5" stroke-width="2.5"><path d="M3 3h42v12c-10 0-14 6-14 14H13v14H3z"/></svg></div>
      <h3>Coving</h3>
      <p>Lorem ipsum dolor sit amet, consectetur adipiscing elit. Etiam auctor tortor tellus, ut consectetur arcu. Nulla consequat egestas dapibus. Nullam eu quam sit amet justo imperdiet viverra. Vivamus leo lacus, interdum ac interdum</p>
    </div>
    <div class="service">
      <div class="disc"><svg width="44" height="44" viewBox="0 0 44 44"><g transform="rotate(-45 22 22)"><rect x="2" y="14" width="40" height="16" rx="8" fill="#3176b5"/><rect x="14" y="16" width="16" height="12" fill="#ececec"/><g fill="#3176b5"><circle cx="18" cy="19" r="1.2"/><circle cx="22" cy="19" r="1.2"/><circle cx="26" cy="19" r="1.2"/><circle cx="18" cy="25" r="1.2"/><circle cx="22" cy="25" r="1.2"/><circle cx="26" cy="25" r="1.2"/></g></g></svg></div>
      <h3>Plasterboarding</h3>
      <p>Lorem ipsum dolor sit amet, consectetur adipiscing elit. Etiam auctor tortor tellus, ut consectetur arcu. Nulla consequat egestas dapibus. Nullam eu quam sit amet justo imperdiet viverra. Vivamus leo lacus, interdum ac interdum</p>
    </div>
  </div>
</section>

<section class="video-block">
  <h2><em>Hollowbrook Renderworks</em> See Recent Video of this Month</h2>
  <div class="wrap video-row">
    <div class="video" role="img" aria-label="Video still of a plasterer skimming a warm-toned wall">
      <div class="play"><svg width="14" height="16" viewBox="0 0 14 16"><path d="M0 0l14 8-14 8z" fill="#fff"/></svg></div>
    </div>
    <div class="video-copy">
      <h3>Nulla consequat egestas dapibus</h3>
      <p>Lorem ipsum dolor sit amet, consectetur adipiscing elit. Etiam auctor tortor tellus, ut consectetur arcu. Nulla consequat egestas dapibus. Nullam eu quam sit amet justo imperdiet viverra. Vivamus leo lacus, interdum ac interdum</p>
      <div class="btn-free">Free Consultan</div>
    </div>
  </div>
</section>

<section class="projects">
  <h2 class="section-title">Our Recent Projects</h2>
  <p>Lorem ipsum dolor sit amet, consectetur adipiscing elit. Etiam auctor tortor tellus, ut consectetur arcu.</p>
  <div class="wrap project-strip">
    <div class="p1" role="img" aria-label="Stone house with round tower under renovation"></div>
    <div class="p2" role="img" aria-label="Tudor style black and white timber house"></div>
    <div class="p3" role="img" aria-label="Brick house wall with newly rendered base"></div>
    <div class="p4" role="img" aria-label="Worker in hard hat plastering a ceiling"></div>
  </div>
</section>

<section class="testimonials">
  <h2 class="section-title">Client Testimonials</h2>
  <h4>Marcus Hale</h4>
  <p>Lorem ipsum dolor sit amet, consectetur adipiscing elit. Etiam auctor tortor tellus, ut consectetur arcu. Nulla consequat egestas dapibus. Nullam eu quam sit amet justo imperdiet viverra. Vivamus leo lacus, interdum ac interdum</p>
  <div class="dots"><i></i><i></i><i></i></div>
</section>

<footer class="footer">
  <div class="wrap footer-cols">
    <div>
      <h5>About Hollowbrook Renderworks</h5>
      <p>Phasellus justo elit, vulputate interdum<br>posuere eu, laoreet eget nibh. Aenean ut<br>dapibus nisl. Vestibulum eu odio faucibus ligula<br>vehicula iaculis. Maecenas augue sapien,<br>posuere eu congue vitae, facilisis quis massa.<br>Maecenas in risus lacus, quis feugiat enim.<br>Maecenas ut orci libero.</p>
    </div>
    <div>
      <h5>Plastering Servies</h5>
      <ul><li>Plastering</li><li>Ceilings</li><li>Coving</li><li>Plasterboarding</li></ul>
    </div>
    <div>
      <h5>Latest Article</h5>
      <div class="article"><div class="thumb"></div><div><b>Plasterer in Hook</b><small><svg width="11" height="11" viewBox="0 0 11 11" fill="none" stroke="#555"><circle cx="5.5" cy="5.5" r="4.5"/><path d="M5.5 3v3h2"/></svg>12 January 2016</small></div></div>
      <div class="article"><div class="thumb" style="background:linear-gradient(135deg,#bbb,#776)"></div><div><b>Plasterer in Surrey</b><small><svg width="11" height="11" viewBox="0 0 11 11" fill="none" stroke="#555"><circle cx="5.5" cy="5.5" r="4.5"/><path d="M5.5 3v3h2"/></svg>5 Nov 2015</small></div></div>
      <div class="article"><div class="thumb" style="background:linear-gradient(135deg,#333,#a88)"></div><div><b>Plasterer in Upton Grey</b><small><svg width="11" height="11" viewBox="0 0 11 11" fill="none" stroke="#555"><circle cx="5.5" cy="5.5" r="4.5"/><path d="M5.5 3v3h2"/></svg>22 Dec 2015</small></div></div>
    </div>
    <div>
      <h5>Contact details</h5>
      <p>Vulputate interdum posuere eu,<br>Unit 15, ligula vehicula</p>
    </div>
  </div>
  <div class="footer-bottom">
    <span>Hollowbrook Renderworks- Copyright © 2016. All Rights Reserved</span>
    <div class="social"><i></i><i></i><i></i><i></i></div>
  </div>
</footer>

</body>
</html>
```